Website Design - Photo Shop Design - Functional Cash Register Layout for POS System

Design a webpage for Point of Sale site. A cash register page.

Page must have a good look. I have attached a file of a possible layout example - but need a much nicer design. I have also attached the site logo. which i will upload without background tomorrow hopefully.

Looking for a nice Fresh look , not dark and dingy.

Target Market(s)

Business

Industry/Entity Type

Business Software

Number of Pages Required

1 page

Colors
f59195
f04a50
ec1f27
fbd4d5
ffffff
f8f3f8
fdf0f6
feeeee
ecf5f6

Requirements
Must have
• Cash register layout for POS software site. Nice layout ,
Nice to have
• Try putting he register part on the left side as well as the right - invert the designs have them different to the layout example shown too.
Should not have
• Not to dark

```html
<!DOCTYPE html>
<html lang="en">
<head>
<meta charset="utf-8">
<title>TillNest – Cash Register</title>
<link href="https://fonts.googleapis.com/css2?family=Open+Sans:wght@400;600;700&display=swap" rel="stylesheet">
<style>
:root{
  --red:#ec1f27;
  --red-soft:#f04a50;
  --pink-light:#fbd4d5;
  --pink-panel:#feeeee;
  --side-bg:#f8f3f8;
  --main-bg:#ecf5f6;
  --white:#ffffff;
  --ink:#222;
  --muted:#777;
  --line:#e4e0e4;
  --grey-btn:#5f6165;
}
*{box-sizing:border-box;margin:0;padding:0}
html,body{width:1200px;height:865px;overflow:hidden}
body{position:relative;font-family:'Open Sans',sans-serif;background:var(--main-bg);color:var(--ink)}
.abs{position:absolute}
.header{left:0;top:0;width:1200px;height:82px;background:var(--white);border-bottom:1px solid #e6e6e6}
.brand{left:33px;top:26px;display:flex;align-items:center;gap:8px}
.brand-mark{width:26px;height:26px;border-radius:50%;background:var(--red)}
.brand-name{font-size:26px;font-weight:700;color:var(--red);letter-spacing:-0.5px;line-height:1}
.brand-sub{left:182px;top:57px;font-size:6px;color:var(--muted)}
.register-btn{left:989px;top:32px;width:140px;height:27px;border:1px solid var(--red);color:var(--red);font-size:8.5px;font-weight:700;display:flex;align-items:center;justify-content:center;letter-spacing:.2px}
.menu-btn{left:1138px;top:31px;width:28px;height:28px;border-radius:50%;border:1px solid #ccc;display:flex;align-items:center;justify-content:center}
.sidebar{left:0;top:82px;width:185px;height:723px;background:var(--side-bg);border-right:1px solid var(--line)}
.nav-active{left:0;top:82px;width:185px;height:61px;background:var(--red-soft);color:var(--white)}
.nav-item{left:33px;width:152px;height:20px;display:flex;align-items:center;gap:9px;font-size:9.5px;text-transform:uppercase}
.nav-item svg{width:12px;height:12px;flex:none}
.nav-sep{left:33px;width:152px;height:1px;background:var(--line)}
.store-badge{left:33px;top:450px;width:131px;height:46px;background:#111;border-radius:5px}
.search{left:209px;top:112px;width:683px;height:28px;background:var(--white);border:1px solid #ddd;font-size:9.5px;color:#aaa;padding:0 11px;display:flex;align-items:center}
.search-btn{left:892px;top:112px;width:35px;height:28px;background:var(--grey-btn);display:flex;align-items:center;justify-content:center}
.tile{width:93px;height:103px;background:var(--white);border:1px solid #e1e1e1}
.tile-code{height:79px;background:var(--red);color:var(--white);font-size:32px;display:flex;align-items:center;justify-content:center}
.tile-name{height:24px;font-size:9.5px;display:flex;align-items:center;justify-content:center;white-space:nowrap}
.pager{top:645px;width:46px;height:28px;background:var(--white);border:1px solid #e1e1e1;font-size:9px;color:#aaa;display:flex;align-items:center;justify-content:center}
.cat-bar{left:209px;top:685px;width:718px;height:27px;background:var(--red-soft);color:var(--white);display:flex;align-items:center;font-size:9.5px}
.cat-bar span{height:27px;display:flex;align-items:center;padding:0 17px;border-right:1px solid rgba(255,255,255,.25)}
.cart{left:951px;top:112px;width:215px;height:573px;background:var(--pink-panel);border:1px solid var(--pink-light)}
.cart-head{left:951px;top:112px;width:215px;height:38px;background:var(--red-soft);color:var(--white);font-size:9.5px;line-height:12px}
.notes{left:965px;top:619px;font-size:10.5px;color:var(--red)}
.totals{left:951px;top:643px;width:215px;text-align:center;font-size:9px;color:var(--muted);line-height:16px}
.btn{top:685px;height:27px;font-size:8.5px;color:var(--white);display:flex;align-items:center;justify-content:center}
.chat{left:1140px;top:732px;width:26px;height:26px;border-radius:50%;background:var(--red);display:flex;align-items:center;justify-content:center}
.footer{left:0;top:805px;width:1200px;height:60px;background:var(--white);border-top:1px solid #e6e6e6;font-size:8.5px;color:var(--muted)}
</style>
</head>
<body>
<header class="abs header">
  <div class="abs brand"><span class="brand-mark"></span><span class="brand-name">TillNest</span></div>
  <div class="abs brand-sub">powered by Kovo</div>
  <div class="abs register-btn">MY SHOP / CASH REGISTER 1</div>
  <div class="abs menu-btn"><svg width="11" height="10" viewBox="0 0 11 10"><rect y="0" width="11" height="2" fill="#ec1f27"/><rect y="4" width="11" height="2" fill="#ec1f27"/><rect y="8" width="11" height="2" fill="#ec1f27"/></svg></div>
</header>

<nav class="abs sidebar"></nav>
<div class="abs nav-active"></div>
<div class="abs nav-item" style="top:108px;color:#fff"><svg viewBox="0 0 12 12"><path d="M6 1 0 6h2v5h3V8h2v3h3V6h2z" fill="#fff"/></svg>Enter Sale</div>
<div class="abs nav-item" style="top:164px"><svg viewBox="0 0 12 12"><path d="M5 0h2v5h2L6 8 3 5h2zM0 8h2v2h8V8h2v4H0z" fill="#222"/></svg>Parked / Layby Orders</div>
<div class="abs nav-sep" style="top:200px"></div>
<div class="abs nav-item" style="top:221px"><svg viewBox="0 0 12 12"><path d="M1 0h1.5v12H1zM3 1h8l-2 3 2 3H3z" fill="#222"/></svg>Completed Sales</div>
<div class="abs nav-sep" style="top:258px"></div>
<div class="abs nav-item" style="top:277px"><svg viewBox="0 0 12 12"><rect x="0.5" y="2" width="11" height="9.5" fill="none" stroke="#222"/><rect x="0.5" y="2" width="11" height="2.5" fill="#222"/><rect x="3" y="0" width="1.5" height="3" fill="#222"/><rect x="7.5" y="0" width="1.5" height="3" fill="#222"/><path d="M2 6h2v1.5H2zM5 6h2v1.5H5zM8 6h2v1.5H8zM2 8.5h2V10H2zM5 8.5h2V10H5z" fill="#222"/></svg>Appointments</div>
<div class="abs nav-sep" style="top:313px"></div>
<div class="abs nav-item" style="top:333px"><svg viewBox="0 0 12 12"><circle cx="6" cy="3.5" r="3" fill="#222"/><path d="M1 12c0-4 2-5.5 5-5.5s5 1.5 5 5.5z" fill="#222"/></svg>Back Office</div>
<div class="abs nav-sep" style="top:370px"></div>
<div class="abs nav-item" style="top:390px"><svg viewBox="0 0 12 12"><path d="M10 4A4.5 4.5 0 0 0 2 3.5M2 8a4.5 4.5 0 0 0 8 .5" fill="none" stroke="#222" stroke-width="1.6"/><path d="M11 1v4H7zM1 11V7h4z" fill="#222"/></svg>Refresh Data</div>
<div class="abs nav-sep" style="top:430px"></div>
<div class="abs store-badge" role="img" aria-label="App download badge"></div>

<main>
  <div class="abs search">Search Product by Name (or) Sku</div>
  <div class="abs search-btn"><svg width="14" height="14" viewBox="0 0 14 14"><circle cx="6" cy="6" r="4.8" fill="none" stroke="#fff" stroke-width="1.3"/><path d="M9.5 9.5 13 13" stroke="#fff" stroke-width="1.3"/></svg></div>

  <div class="abs tile" style="left:209px;top:162px"><div class="tile-code">DP</div><div class="tile-name">Demo Product</div></div>
  <div class="abs tile" style="left:313px;top:162px"><div class="tile-code">EL</div><div class="tile-name">Entry Level Comp...</div></div>
  <div class="abs tile" style="left:416px;top:162px"><div class="tile-code">GC</div><div class="tile-name">Gift Card</div></div>
  <div class="abs tile" style="left:521px;top:162px"><div class="tile-code">P5</div><div class="tile-name">Product 5</div></div>
  <div class="abs tile" style="left:625px;top:162px"><div class="tile-code">T2</div><div class="tile-name">Test 2</div></div>
  <div class="abs tile" style="left:729px;top:162px"><div class="tile-code">T3</div><div class="tile-name">Test 3</div></div>
  <div class="abs tile" style="left:833px;top:162px"><div class="tile-code">FA</div><div class="tile-name">fasdfadfasdf</div></div>
  <div class="abs tile" style="left:520px;top:278px"><div class="tile-code">T6</div><div class="tile-name">Test 6</div></div>

  <div class="abs pager" style="left:209px">« Prev</div>
  <div class="abs pager" style="left:882px">Next »</div>

  <div class="abs cat-bar">
    <span style="padding:0 14px">&#8249;</span><span>LIST ALL</span><span>DEALS</span><span>UNCATEGORIZED</span>
    <span style="margin-left:auto;border:none">&#8250;</span>
  </div>

  <aside class="abs cart"></aside>
  <div class="abs cart-head">
    <svg class="abs" style="left:13px;top:9px" width="18" height="20" viewBox="0 0 18 20"><circle cx="9" cy="5" r="4.5" fill="#fff"/><path d="M0 20c0-7 3-9.5 9-9.5s9 2.5 9 9.5z" fill="#fff"/></svg>
    <div class="abs" style="left:40px;top:7px">Select<br>Customer</div>
    <div class="abs" style="left:122px;top:0;width:1px;height:38px;background:rgba(255,255,255,.3)"></div>
    <div class="abs" style="right:12px;top:7px;text-align:right">Transaction#<br>00016</div>
  </div>
  <div class="abs notes">Add Notes</div>
  <div class="abs totals">Subtotal : $0.00 | Tax : $0.00 | Total : $0.00<br>Paid : $0.00</div>
  <div class="abs btn" style="left:951px;width:29px;background:var(--grey-btn);font-size:13px;font-weight:700">+</div>
  <div class="abs btn" style="left:981px;width:95px;background:var(--grey-btn)">SAVE &amp; PARK / LAYBY</div>
  <div class="abs btn" style="left:1096px;width:70px;background:var(--red);justify-content:space-between;padding:0 7px 0 11px"><span>PAY</span><span>$0.00</span></div>
  <div class="abs chat"><svg width="14" height="12" viewBox="0 0 14 12"><ellipse cx="5.5" cy="5" rx="5" ry="4" fill="#fff"/><ellipse cx="9.5" cy="7" rx="4" ry="3.2" fill="#fff" stroke="#ec1f27" stroke-width=".8"/></svg></div>
</main>

<footer class="abs footer">
  <div class="abs" style="left:0;top:26px;width:1200px;text-align:center">COPYRIGHTS © TILLNEST | ALLRIGHTS RESERVED.</div>
  <div class="abs" style="left:1153px;top:26px">C11</div>
</footer>
</body>
</html>
```